Motorcycle Shop Business Card

New business card for Motorcycle repair and customization shop.Business name: Copper Falcon Chris Morris443-865-5190, 7214 Quarry Lane Arbutus, MD 21227. www.dale@copperfalconcustoms.example. I uploaded some motorcycle images and logo and a couple of our calendar shoots. They do not have to be used on card just examples of some of our work and past graphic work.
We work on Vantor Brennick and Custom Built Motorcycles.

Looking for front and back design

Target Market(s)

Motorcycle owners

Industry/Entity Type

Motorcycle Part

```html
<!DOCTYPE html>
<html lang="en">
<head>
<meta charset="utf-8">
<title>Copper Falcon Customs – Business Card</title>
<link href="https://fonts.googleapis.com/css2?family=Montserrat:wght@400;600&family=Michroma&display=swap" rel="stylesheet">
<style>
  :root {
    --backdrop: #141414;
    --card: #0a0a0a;
    --mesh-dark: #1a1a1a;
    --ink: #ffffff;
    --ink-soft: #d9d9d9;
    --icon: #9a9a9a;
  }
  * { margin: 0; padding: 0; box-sizing: border-box; }
  html, body { width: 1200px; height: 1200px; overflow: hidden; }
  body {
    background: radial-gradient(ellipse at center, #1c1c1c 0%, var(--backdrop) 70%);
    font-family: "Montserrat", sans-serif;
    color: var(--ink);
    position: relative;
  }
  .card {
    position: absolute;
    left: 140px;
    width: 920px;
    height: 526px;
    background: var(--card);
    border-radius: 22px;
    overflow: hidden;
    box-shadow: 0 18px 40px rgba(0,0,0,.6);
  }
  .card--front { top: 50px; }
  .card--back { top: 622px; }
  .mesh-texture {
    position: absolute;
    right: 0; top: 0;
    width: 68%;
    height: 100%;
    background:
      radial-gradient(ellipse 55% 70% at 35% 45%, rgba(150,150,150,.55) 0%, rgba(60,60,60,.25) 45%, transparent 75%),
      linear-gradient(90deg, var(--card) 0%, var(--mesh-dark) 30%, #2a2a2a 60%, #151515 100%);
    -webkit-mask-image: linear-gradient(90deg, transparent 0%, #000 35%);
            mask-image: linear-gradient(90deg, transparent 0%, #000 35%);
  }
  .brand {
    position: absolute;
    font-weight: 600;
    color: var(--ink);
    line-height: 1.05;
    font-size: 46px;
    letter-spacing: 1px;
  }
  .card--front .brand { left: 90px; top: 250px; }
  .card--back .brand { left: 110px; top: 80px; }
  .brand span { display: block; }
  .holder-name {
    position: absolute;
    left: 110px; top: 320px;
    font-family: "Michroma", sans-serif;
    font-weight: 400;
    font-size: 27px;
    letter-spacing: 2px;
  }
  .rule {
    position: absolute;
    height: 1.5px;
    background: var(--ink-soft);
  }
  .rule--name { left: 110px; top: 366px; width: 710px; }
  .rule--address { right: 100px; top: 440px; width: 300px; }
  .contact {
    position: absolute;
    left: 110px; top: 384px;
    list-style: none;
    font-size: 19px;
    color: var(--ink-soft);
    white-space: nowrap;
  }
  .contact li { display: flex; align-items: center; gap: 14px; height: 36px; }
  .contact svg { width: 20px; height: 20px; fill: var(--icon); flex: none; }
  .address {
    position: absolute;
    right: 100px; top: 452px;
    font-size: 19px;
    color: var(--ink-soft);
    white-space: nowrap;
  }
</style>
</head>
<body>
  <section class="card card--front">
    <div class="mesh-texture" role="img" aria-label="Dark hexagonal metal mesh texture with soft highlight"></div>
    <div class="brand"><span>Copper Falcon</span><span>Customs</span></div>
  </section>

  <section class="card card--back">
    <div class="mesh-texture" role="img" aria-label="Dark hexagonal metal mesh texture with soft highlight"></div>
    <div class="brand"><span>Copper Falcon</span><span>Customs</span></div>
    <h1 class="holder-name">DALE FENWICK</h1>
    <div class="rule rule--name"></div>
    <ul class="contact">
      <li>
        <svg viewBox="0 0 24 24" aria-hidden="true"><path d="M3 8c0-2 2-3 9-3s9 1 9 3v2h-5V8H8v2H3zM6 11h12l2 8H4z"/></svg>
        410-555-0137, 7214
      </li>
      <li>
        <svg viewBox="0 0 24 24" aria-hidden="true"><path d="M2 5h20v14H2zm2 2v.5l8 5.5 8-5.5V7z"/></svg>
        Dale@copperfalconcustoms.example
      </li>
    </ul>
    <div class="rule rule--address"></div>
    <p class="address">Quarry Lane Arbutus, MD 21227</p>
  </section>
</body>
</html>
```